University Entrepreneurship Housing Cohort Needs a Flyer Design

Wrenfield College's Venture and Discovery Center needs a flyer designed for their new "V-Nest" (short for Venture Nest) Living Learning Community.

The purpose of the V-Nest Residential Cohort (RC) is to provide students at Wrenfield College with the opportunity to live, learn, and participate in activities that have an Venture and Discovery Center focus. Students with entrepreneurial ambitions will be able to connect with others who share those similar interests and aspirations. The community will create a space for students to learn about entrepreneurial and innovative ways of thinking and working, and to begin to implement their ideas using RC provided resources (e.g,, workshops, site visits, mentors, and peer-networking). The RC will also include an on-site V-Nest Commons, which functions as a study space for V-Nest students. The lounge will have dry-erase walls, a 65-inch touch screen monitor, internet connectivity, and printing capabilities. The final design should communicate an exciting and innovative focused opportunity for young college students.

Note: Both logos need to be on the flyer, but pictures can be selected additionally as desired.

Target Market(s)

Undergraduate students who plan to live in on campus housing and have an interest in Venture and Discovery Center

Industry/Entity Type

University

Font styles to use
Sans Serif

Requirements
Must have
• Both logos need to be on the flyer, but pictures can be selected additionally as desired.
• Font: Gill Sans (for larger text) and Usherwood (for smaller text)
• The purpose of the Venture Nest (V-Nest) Living Learning Community (RC) is to provide students at Wrenfield College with the opportunity to live, learn, and participate in activities that have an Venture and Discovery Center focus.
• Students with entrepreneurial ambitions will be able to connect with others who share similar interests and aspirations. Using resources provided by the V-Nest RC and the Venture and Discovery Center, residents will begin to develop their ideas, as well as participate in experiences that include workshops, competitions, mentorship, exposure to the Atlanta ecosystem, and peer-to-peer networking.
• The V-Nest Commons will include:
• - Collaborative study space
• - Dry-erase walls
• - 65-inch touchscreen monitor
• - Internet connectivity
• - Printing capabilities
• Website: vdc.wrenfield-example.edu
• Phone: 555-208-3164
• Twitter: @WCVDCtr
• Facebook: WC_VDCtr
• LinkedIn: Venture & Discovery Center at Wrenfield College
Nice to have
• Color codes:
• Blue PMS 286
• RED PMS 186
• Grey PMS 404
• More details here: http://brandpack.wrenfield-example.edu/guidelines/visual-identity/type-color-usage/

```html
<!DOCTYPE html>
<html lang="en">
<head>
<meta charset="utf-8">
<title>V-Nest Flyer</title>
<link href="https://fonts.googleapis.com/css2?family=Open+Sans:ital,wght@0,400;0,600;0,700;1,400&display=swap" rel="stylesheet">
<style>
  :root{
    --blue:#0039a6;
    --blue-deep:#1a3f8f;
    --red:#c8102e;
    --grey:#6b6560;
    --ink:#4a4a4a;
    --paper:#ffffff;
    --paper-shade:#eeeeef;
    --band:#3a3a3c;
    --stage:#d9d9db;
  }
  *{margin:0;padding:0;box-sizing:border-box;}
  html,body{width:1200px;height:800px;overflow:hidden;}
  body{background:var(--stage);font-family:"Open Sans",sans-serif;color:var(--ink);position:relative;}

  .flyer{position:absolute;left:306px;top:20px;width:588px;height:760px;overflow:hidden;
    background:linear-gradient(160deg,var(--paper) 55%,var(--paper-shade));box-shadow:0 4px 18px rgba(0,0,0,.2);}

  .band{position:absolute;inset:0;}

  .photo{position:absolute;border:6px solid var(--paper);border-radius:4px;}
  .photo--lounge-top{left:340px;top:-6px;width:254px;height:92px;background:linear-gradient(135deg,#9aa4ad,#3d4650 60%,#7a2f35);}
  .photo--map-chat{left:330px;top:88px;width:264px;height:140px;background:linear-gradient(120deg,#e7d9c5,#d8b9a6 45%,#b8453e);}
  .photo--laptop{left:420px;top:240px;width:174px;height:144px;background:linear-gradient(135deg,#c9a24a,#3a2d28 50%,#c9c23a);}
  .photo--sofa{left:400px;top:390px;width:194px;height:152px;background:linear-gradient(150deg,#a9c6d6,#7b3a2e 55%,#3e4a52);}
  .photo--entrance{left:470px;top:550px;width:124px;height:150px;background:linear-gradient(160deg,#b9c3cc,#8c4a3a 50%,#5b5e66);}

  .brand{position:absolute;left:40px;top:108px;display:flex;align-items:center;gap:12px;}
  .brand__dot{width:30px;height:30px;border-radius:50%;background:var(--blue-deep);}
  .brand__name{font-size:42px;font-weight:700;color:var(--blue-deep);letter-spacing:.5px;line-height:1.2;}

  .copy{position:absolute;left:40px;top:172px;width:280px;font-size:11.5px;line-height:1.45;}
  .copy p+p{margin-top:10px;}
  .copy strong{font-weight:700;color:#333;}

  .amenities{position:absolute;left:0;top:380px;}
  .amenities__lead{font-size:14px;color:var(--blue);margin:0 0 6px 40px;}
  .amenities__list{list-style:none;}
  .amenities__list li{height:24px;margin-bottom:5px;background:var(--blue);color:#fff;font-size:12px;font-weight:600;
    letter-spacing:.6px;text-transform:uppercase;line-height:24px;padding-left:40px;border-radius:0 14px 14px 0;}

  .partner{position:absolute;left:40px;top:562px;display:flex;align-items:center;gap:14px;}
  .partner__college{font-size:22px;font-weight:400;color:var(--grey);}
  .partner__rule{width:1px;height:40px;background:var(--grey);}
  .partner__unit{font-size:13px;letter-spacing:1px;line-height:1.3;color:var(--grey);text-transform:uppercase;}

  .contact{position:absolute;left:40px;top:622px;font-size:11px;line-height:1.5;display:grid;grid-template-columns:60px 1fr;column-gap:10px;}
  .contact dt{font-weight:700;color:var(--grey);}
  .social{position:absolute;left:40px;top:670px;list-style:none;font-size:10.5px;}
  .social li{display:flex;align-items:center;gap:6px;margin-bottom:4px;}
  .social__dot{width:13px;height:13px;border-radius:50%;background:var(--blue);}
</style>
</head>
<body>
<main class="flyer">
  <svg class="band" width="588" height="760" viewBox="0 0 588 760" aria-hidden="true">
    <polygon points="360,0 588,0 588,640 420,300" fill="var(--band)"/>
  </svg>

  <div class="photo photo--lounge-top" role="img" aria-label="Student relaxing on a sofa in the lounge"></div>
  <div class="photo photo--map-chat" role="img" aria-label="Two students talking in front of a wall map"></div>
  <div class="photo photo--laptop" role="img" aria-label="Two students smiling over a laptop"></div>
  <div class="photo photo--sofa" role="img" aria-label="Students studying on a red sofa by large windows"></div>
  <div class="photo photo--entrance" role="img" aria-label="Students at the residence hall entrance"></div>

  <div class="brand">
    <span class="brand__dot"></span>
    <span class="brand__name">V-Nest</span>
  </div>

  <section class="copy">
    <p>The <strong>purpose</strong> of the <strong>V-Nest</strong> Residential Cohort (RC) is to provide undergraduate students at Wrenfield College with the opportunity to live, learn, and participate in activities that have an entrepreneurship and innovation focus.</p>
    <p>The community will create a space for students to learn about entrepreneurial and innovative ways of thinking and working, and to begin to implement their ideas using RC provided resources.</p>
  </section>

  <section class="amenities">
    <p class="amenities__lead">The lounge will have...</p>
    <ul class="amenities__list">
      <li style="width:300px">Collaborative study space</li>
      <li style="width:280px">Dry-erase walls</li>
      <li style="width:345px">A 65-inch touch screen monitor</li>
      <li style="width:310px">Internet connectivity</li>
      <li style="width:320px">Printing capabilities</li>
    </ul>
  </section>

  <div class="partner">
    <span class="partner__college">Wrenfield College</span>
    <span class="partner__rule"></span>
    <span class="partner__unit">Venture and<br>Discovery Center</span>
  </div>

  <dl class="contact">
    <dt>Website</dt><dd>vdc.wrenfield-example.edu</dd>
    <dt>Phone</dt><dd>555-208-3164</dd>
  </dl>

  <ul class="social">
    <li><span class="social__dot"></span>@WCVDCtr</li>
    <li><span class="social__dot"></span>WC_VDCtr</li>
    <li><span class="social__dot"></span>Venture &amp; Discovery Center at Wrenfield College</li>
  </ul>
</main>
</body>
</html>
```